Website for Velmorund Capital, my new firm that raises money from investors to buy, build, own an...

Velmorund Capital needs a website! We are a new company with very experienced people, who invest in, own and build hotel properties, as well as apartments and other commercial real estate. We seek investors for our projects, and we provide safe, secure returns on their investment in our projects. Our new logo is designed to exhibit strength, class and security, and would like our website to continue on this theme. Our name, Velmorund, is a word-play on a Greek word “aristeia”, which means “excellence” and “a warriors finest moment of glory in war”. If you are in business, you realize that much of it is like war, with strategy and moves and opponents and competitors, and ever-changing economic conditions and threats that make business very much like war. We like to think that we are good at business (war), and so have named our company “Velmorund”, using the founders last name and the word “aristeia” combined. Another definition of "aristeia" is "performing at the peak of one's potential after a long struggle"...again, much like business in real life! The website design should exhibit financial security, smart moves, and positive growth towards a bright future.

Target Market(s)

The target market is smart and wealthy investors, with others such as brokers, cities and government agencies, lenders, sellers, partners, etc also looking at it.

Industry/Entity Type

Investment

Number of Pages Required

5+ page

Font styles to use
Sans Serif

Colors
fec214

Requirements
Must have
• Our website should have a landing page, a "about" or bio page, a projects page and a contact us page. Our new logo uses the colors black and gold, so this should be factored in to our site. The site should be simple, yet impactful and impressive. I have actually two logos, which can be mixed and interchanged in a complimentary way, each with their own unique look.
Nice to have
• I have uploaded a couple screenshots of a website i like, and the simplicity I mention.
Should not have
• The site should not be flashy or complicated or complex or "busy"

```html
<!DOCTYPE html>
<html lang="en">
<head>
<meta charset="utf-8">
<title>Velmorund Capital</title>
<link href="https://fonts.googleapis.com/css2?family=Lato:wght@400;700;900&display=swap" rel="stylesheet">
<style>
:root{
  --gold:#c9a85a;
  --gold-soft:#d6b86e;
  --ink:#1b1b1b;
  --text:#222222;
  --hero-bg:#f2f2f2;
  --white:#ffffff;
  --panel:rgba(58,58,58,0.86);
  --footer:#1c1c1c;
}
*{margin:0;padding:0;box-sizing:border-box}
html,body{width:1200px;height:4833px;overflow:hidden;background:var(--white)}
body{position:relative;font-family:'Lato',sans-serif;color:var(--text)}
.abs{position:absolute}
.center{left:0;width:1200px;text-align:center}

/* nav */
.nav-link{top:50px;font-size:17px;font-weight:900;letter-spacing:.5px;color:var(--ink);text-decoration:none}
.brand{left:520px;top:22px;width:160px;height:76px;display:flex;flex-direction:column;align-items:center;justify-content:center;gap:6px}
.brand-mark{width:14px;height:14px;background:var(--gold)}
.brand-name{font-size:20px;font-weight:900;letter-spacing:1px;color:var(--ink)}

/* hero */
.hero{left:0;top:0;width:1200px;height:790px;background:var(--hero-bg)}
.eyebrow{font-size:23px;font-weight:700;letter-spacing:1.5px;color:var(--ink)}
.hero-title{top:325px;font-size:46px;font-weight:900;line-height:60px;color:var(--ink)}
.hero-copy{top:453px;font-size:19px;font-weight:700;line-height:28px;color:var(--ink)}
.scroll-cue{left:567px;top:653px;width:256px;height:150px;background:var(--gold-soft);display:flex;align-items:center;justify-content:center}

/* headings */
.section-label{font-size:24px;font-weight:900;letter-spacing:2px}
.rule{width:100px;height:4px;background:var(--gold);left:550px}
.light{color:var(--white)}

/* services */
.service{width:220px;text-align:center}
.service-icon{display:block;margin:0 auto}
.service-name{margin-top:22px;font-size:18px;font-weight:900;color:var(--ink)}

/* buttons */
.btn{display:flex;align-items:center;justify-content:center;font-size:20px;font-weight:700;letter-spacing:2px;text-decoration:none}
.btn-outline-dark{border:3px solid var(--ink);color:var(--ink)}
.btn-outline-light{border:3px solid #e6e6e6;color:var(--white)}
.btn-outline-gold{border:3px solid var(--gold);color:var(--gold)}
.btn-gold{background:var(--gold);color:var(--white)}

/* photo bands */
.photo{left:0;width:1200px}
.photo-keys{top:1483px;height:657px;background:linear-gradient(120deg,#5e5e5e 0%,#a9a9a9 45%,#7a7a7a 70%,#cfcfcf 100%)}
.photo-chess{top:2960px;height:817px;background:linear-gradient(160deg,#1f1f1f 0%,#3c3c3c 45%,#5d5d5d 75%,#2a2a2a 100%)}
.photo-sunset{top:3777px;height:823px;background:linear-gradient(180deg,#7d7040 0%,#8e7e45 40%,#a68c4d 70%,#5a4b2a 100%)}

.panel{left:173px;top:1627px;width:854px;height:556px;background:var(--panel)}
.panel-wedge{left:173px;top:1627px}

.band-title{font-size:38px;font-weight:900;line-height:50px;color:var(--white)}
.band-copy{font-size:18px;font-weight:700;line-height:29px;color:var(--white)}

/* about */
.quote{top:2360px;font-size:40px;font-weight:900;line-height:50px;color:var(--ink)}
.about-copy{top:2545px;font-size:18px;font-weight:700;line-height:29px;color:var(--ink)}
.founder{top:2655px;font-size:20px;font-weight:900;color:var(--ink)}
.founder-role{top:2685px;font-size:15px;font-weight:900;letter-spacing:1px;color:var(--gold)}

/* footer */
.footer{left:0;top:4600px;width:1200px;height:233px;background:var(--footer)}
.address{left:190px;top:4675px;font-size:17px;font-weight:900;line-height:22px;color:var(--white)}
.social{left:620px;top:4632px;width:390px;display:flex;justify-content:space-between;font-size:16px;font-weight:900;color:var(--white)}
.partner-badge{left:917px;top:4693px;width:83px;height:54px;background:#f0f0f0}
.copyright{left:700px;top:4765px;width:300px;text-align:right;font-size:15px;font-weight:900;color:var(--white)}
</style>
</head>
<body>

<!-- hero -->
<section class="abs hero" aria-label="Introduction"></section>
<nav>
  <a class="abs nav-link" style="left:307px" href="#about">ABOUT US</a>
  <a class="abs nav-link" style="left:433px" href="#projects">PROJECT</a>
  <div class="abs brand"><span class="brand-mark"></span><span class="brand-name">VELMORUND</span></div>
  <a class="abs nav-link" style="left:693px" href="#finance">FINANCE</a>
  <a class="abs nav-link" style="left:810px" href="#contact">CONTACT</a>
</nav>
<p class="abs center eyebrow" style="top:232px">THE GOLD OF MANAGEMENT CAPITAL</p>
<h1 class="abs center hero-title">Performing at the peak of one’s<br>potential after a long struggle</h1>
<p class="abs center hero-copy">Lorem ipsum dolor sit amet, consectetur adipiscing elit.<br>Donec pretium nisi malesuada porttitor iaculis. Suspendisse molestie nec sem<br>sed placerat. Nam massa tellus, blandit sed egestas cursus, lacinia id purus.<br>Donec pretium nisi malesuada porttitor iaculis.</p>
<a class="abs scroll-cue" href="#projects" aria-label="Scroll down">
  <svg width="80" height="34" viewBox="0 0 80 34"><polyline points="4,4 40,28 76,4" fill="none" stroke="#1b1b1b" stroke-width="6"/></svg>
</a>

<!-- projects -->
<h2 id="projects" class="abs center section-label" style="top:908px;color:var(--ink);font-size:32px">PROJECT WITH US</h2>
<div class="abs rule" style="top:950px"></div>

<div class="abs service" style="left:140px;top:1043px">
  <svg class="service-icon" width="160" height="160" viewBox="0 0 160 160">
    <circle cx="80" cy="80" r="78" fill="var(--gold)"/><circle cx="80" cy="80" r="66" fill="none" stroke="#fff" stroke-width="4"/>
    <circle cx="68" cy="62" r="14" fill="#fff"/><path d="M40 112a28 28 0 0 1 56 0z" fill="#fff"/>
    <circle cx="104" cy="100" r="16" fill="#fff"/><text x="104" y="107" text-anchor="middle" font-family="Lato,sans-serif" font-weight="900" font-size="20" fill="var(--gold)">$</text>
  </svg>
  <p class="service-name">INVESMENT</p>
</div>
<div class="abs service" style="left:373px;top:1043px">
  <svg class="service-icon" width="160" height="160" viewBox="0 0 160 160">
    <circle cx="80" cy="80" r="78" fill="var(--gold)"/><circle cx="80" cy="80" r="66" fill="none" stroke="#fff" stroke-width="4"/>
    <rect x="46" y="92" width="14" height="22" fill="#fff"/><rect x="66" y="80" width="14" height="34" fill="#fff"/><rect x="86" y="68" width="14" height="46" fill="#fff"/><rect x="106" y="56" width="14" height="58" fill="#fff"/>
    <polyline points="44,80 70,62 90,66 116,44" fill="none" stroke="#fff" stroke-width="4"/>
  </svg>
  <p class="service-name">FINANCE</p>
</div>
<div class="abs service" style="left:607px;top:1043px">
  <svg class="service-icon" width="160" height="160" viewBox="0 0 160 160">
    <circle cx="80" cy="80" r="78" fill="var(--gold)"/><circle cx="80" cy="80" r="66" fill="none" stroke="#fff" stroke-width="4"/>
    <rect x="50" y="46" width="44" height="68" fill="#fff"/>
    <g fill="var(--gold)"><rect x="58" y="54" width="8" height="8"/><rect x="78" y="54" width="8" height="8"/><rect x="58" y="70" width="8" height="8"/><rect x="78" y="70" width="8" height="8"/><rect x="66" y="96" width="12" height="18"/></g>
    <circle cx="106" cy="96" r="16" fill="#fff" stroke="var(--gold)" stroke-width="3"/><text x="106" y="103" text-anchor="middle" font-family="Lato,sans-serif" font-weight="900" font-size="20" fill="var(--gold)">$</text>
  </svg>
  <p class="service-name">PROPERTY</p>
</div>
<div class="abs service" style="left:840px;top:1043px">
  <svg class="service-icon" width="160" height="160" viewBox="0 0 160 160">
    <circle cx="80" cy="80" r="78" fill="var(--gold)"/><circle cx="80" cy="80" r="66" fill="none" stroke="#fff" stroke-width="4"/>
    <path d="M80 42 L122 80 H110 V114 H50 V80 H38 Z" fill="#fff"/><rect x="72" y="92" width="16" height="22" fill="var(--gold)"/>
  </svg>
  <p class="service-name">REAL ESTATE</p>
</div>

<a class="abs btn btn-outline-dark" style="left:440px;top:1353px;width:317px;height:50px" href="#start">HOW TO GET STARTED</a>

<!-- security band -->
<div class="abs photo photo-keys" role="img" aria-label="Black and white photograph of a padlock beside rolled banknotes"></div>
<div class="abs panel"></div>
<svg class="abs panel-wedge" width="854" height="556" viewBox="0 0 854 556"><polygon points="0,430 854,540 854,556 0,556" fill="var(--gold)"/></svg>
<p class="abs center section-label light" style="top:1697px;font-size:22px">SECURE AND PROTECTION</p>
<div class="abs rule" style="top:1733px"></div>
<h2 class="abs center band-title" style="top:1757px">Reliable invesment protection<br>with accurate and always refined analysis<br>information technology</h2>
<a class="abs btn btn-outline-light" style="left:497px;top:1990px;width:206px;height:48px" href="#security">LEARN MORE</a>

<!-- about -->
<p id="about" class="abs center section-label" style="top:2278px;color:var(--ink);font-size:22px">ABOUT US</p>
<div class="abs rule" style="top:2316px"></div>
<blockquote class="abs center quote">“ Building commitment and communication<br>has a strong meaning in building<br>a sustainable business ”</blockquote>
<p class="abs center about-copy">Lorem ipsum dolor sit amet, consectetur adipiscing elit. Donec pretium nisi male-<br>suada porttitor iaculis. Suspendisse molestie nec sem sed placerat. Nam massa<br>tellus, blandit sed egestas cursus, lacinia id purus</p>
<p class="abs center founder">THEO MARLOW</p>
<p class="abs center founder-role">FOUNDER</p>
<a class="abs btn btn-outline-dark" style="left:507px;top:2777px;width:190px;height:50px" href="#team">OUR TEAM</a>

<!-- strategy band -->
<div class="abs photo photo-chess" role="img" aria-label="Dark photograph of a hand moving a piece on a chessboard"></div>
<p class="abs center section-label light" style="top:3093px;font-size:22px">A SMART MOVE</p>
<div class="abs rule" style="top:3130px"></div>
<h2 class="abs center band-title" style="top:3155px">Challenge after challenge in the era of<br>economic war made us strong in running<br>a business with vairous strategies<br>that worked appropriately</h2>
<p class="abs center band-copy" style="top:3390px">Lorem ipsum dolor sit amet, consectetur adipiscing elit. Donec pretium nisi male-<br>suada porttitor iaculis. Suspendisse molestie nec sem sed placerat. Nam massa<br>tellus, blandit sed egestas cursus, lacinia id purus</p>
<a class="abs btn btn-outline-gold" style="left:500px;top:3597px;width:203px;height:47px" href="#strategy">LEARN MORE</a>

<!-- future band -->
<div class="abs photo photo-sunset" role="img" aria-label="Warm photograph of a group standing together in a field at sunset"></div>
<p class="abs center section-label light" style="top:3890px;font-size:22px">INVESMENT FOR THE FUTURE</p>
<div class="abs rule" style="top:3927px"></div>
<h2 class="abs center band-title" style="top:3997px">We and you will always see a lot of<br>opportunities in every challenge by opening<br>the space to coma out staring ahead<br>that is more cheerful</h2>
<p class="abs center band-copy" style="top:4217px">Lorem ipsum dolor sit amet, consectetur adipiscing elit. Donec pretium nisi male-<br>suada porttitor iaculis. Suspendisse molestie nec sem sed placerat. Nam massa<br>tellus, blandit sed egestas cursus, lacinia id purus</p>
<a class="abs btn btn-gold" style="left:333px;top:4437px;width:207px;height:50px" href="#join">JOIN US</a>
<a class="abs btn btn-outline-light" style="left:657px;top:4437px;width:206px;height:50px" href="#contact">CONTACT US</a>

<!-- footer -->
<footer id="contact" class="abs footer"></footer>
<address class="abs address" style="font-style:normal">12 Brassfield Lane<br>Arlington VA, USA<br>T. +1 555 014 2290</address>
<div class="abs social"><span>Pagebook</span><span>Chirpo</span><span>Vidzo</span><span>Netwise</span><span>Plusly</span><span>Xingo</span></div>
<div class="abs partner-badge"></div>
<p class="abs copyright">©2018 Velmorund All Right Reserved</p>

</body>
</html>
```